BrivoMatex. Lantern for the Steady Growth. Business card

Professional business card for BrivoMatex (Lantern for the Steady Growth)
My rationale: Strategy-> Execution-> Results-> Value that lead to the BrivoMatex name: We put the Lantern for the Steady Growth.
We deliver value to our customers helping them at defining a good strategy (cyan arrow). 90% of well formulated strategies fail due to poor execution so we also consider strategical execution very important (green arrow). Due to the execution we obtain the results (blue arrow). Finally, the results provide feedback to redefine strategy, and the new strategy has to be executed and new results obtained providing new feedback and on and on. It's like a wheel that finally, must create corporate value: value for shareholders, staholders, employees, providers...-

Target Market(s)

CEOs and steering comitees , invewrnent funds

Industry/Entity Type

Business Consultant

Contact Information for Business Card

Tommaso Ferlini
CEO & Founder
tommaso.ferlini@brivomatex.example
Mobile: +34 611.205.938
www.brivomatex.example

Colors

Designer to choose colors to be used in the design.

Requirements
Nice to have
• Nice to hace the words: Strategy, execution, results
• Nice to vave the claim: Lantern for the Steady Growth
• The three colors should be shown:
• cyan for STRATEGY
• green for EXECUTION
• blue for RESULTS
Should not have
• Complete black background

```html
<!DOCTYPE html>
<html lang="en">
<head>
<meta charset="utf-8">
<title>BrivoMatex — Business Card</title>
<link rel="stylesheet" href="https://fonts.googleapis.com/css2?family=Roboto+Condensed:wght@400;700&display=swap">
<style>
  :root {
    --backdrop: #e8e3da;
    --brand-blue: #233f93;
    --brand-navy: #1f3a8f;
    --brand-green: #8cc63f;
    --brand-cyan: #36a9e1;
    --card-white: #ffffff;
    --ink: #2b2b2b;
    --font-main: "Roboto Condensed", "Arial Narrow", sans-serif;
  }
  * { box-sizing: border-box; margin: 0; padding: 0; }
  html, body {
    width: 1200px; height: 900px; overflow: hidden;
    background: var(--backdrop);
    font-family: var(--font-main);
  }
  .canvas { position: relative; width: 1200px; height: 900px; }
  .card {
    position: absolute; left: 311px; width: 577px; height: 329px;
    box-shadow: 0 6px 14px rgba(0,0,0,0.18);
  }
  .card--front {
    top: 98px; background: var(--brand-blue);
    display: flex; flex-direction: column; align-items: center; justify-content: center;
    padding-top: 60px;
  }
  .front-name {
    color: var(--card-white); font-weight: 700; font-size: 54px;
    letter-spacing: -0.5px; line-height: 1;
  }
  .front-claim {
    margin-top: 6px; color: var(--brand-green); font-weight: 400;
    font-size: 16.5px; letter-spacing: 0.3px; text-transform: uppercase;
  }
  .front-pillars {
    margin-top: 4px; color: var(--brand-cyan); font-size: 16.5px;
    letter-spacing: 0.6px; text-transform: uppercase; word-spacing: 3px;
  }
  .card--back { top: 472px; background: var(--card-white); }
  .back-name {
    position: absolute; left: 44px; top: 190px;
    color: var(--brand-navy); font-weight: 700; font-size: 36px;
    letter-spacing: -0.5px; line-height: 1;
  }
  .divider {
    position: absolute; left: 254px; top: 106px; width: 2px; height: 116px;
    background: var(--brand-navy);
  }
  .contact { position: absolute; left: 282px; top: 104px; }
  .contact-name {
    color: var(--brand-navy); font-weight: 700; font-size: 17px;
    letter-spacing: 0.4px; text-transform: uppercase;
  }
  .contact-role { margin-top: 2px; color: var(--ink); font-size: 12px; text-transform: uppercase; }
  .contact-list { list-style: none; margin-top: 14px; }
  .contact-item {
    display: flex; align-items: center; gap: 6px; height: 24px;
    color: var(--ink); font-size: 14.5px;
  }
  .contact-icon { width: 17px; height: 17px; fill: var(--brand-navy); flex: none; }
</style>
</head>
<body>
<main class="canvas">
  <section class="card card--front">
    <div class="front-name">BrivoMatex</div>
    <div class="front-claim">Lantern for the Steady Growth</div>
    <div class="front-pillars">Strategy | Execution | Results</div>
  </section>

  <section class="card card--back">
    <div class="back-name">BrivoMatex</div>
    <div class="divider"></div>
    <div class="contact">
      <div class="contact-name">Tommaso Ferlini</div>
      <div class="contact-role">CEO &amp; Founder</div>
      <ul class="contact-list">
        <li class="contact-item">
          <svg class="contact-icon" viewBox="0 0 16 16" aria-hidden="true"><path d="M4 0h8a1.5 1.5 0 0 1 1.5 1.5v13A1.5 1.5 0 0 1 12 16H4a1.5 1.5 0 0 1-1.5-1.5v-13A1.5 1.5 0 0 1 4 0zm0.5 2v10.5h7V2zm3.5 11.2a0.9 0.9 0 1 0 0 1.8 0.9 0.9 0 0 0 0-1.8z"/></svg>
          <span>+34 611.205.938</span>
        </li>
        <li class="contact-item">
          <svg class="contact-icon" viewBox="0 0 16 16" aria-hidden="true"><path d="M0 3h16v10H0zM1.5 4.5v0.4L8 9l6.5-4.1v-0.4zM1.5 6.6v4.9h13V6.6L8 10.8z"/></svg>
          <span>tommaso.ferlini@brivomatex.example</span>
        </li>
        <li class="contact-item">
          <svg class="contact-icon" viewBox="0 0 16 16" aria-hidden="true"><path d="M8 0a8 8 0 1 0 0 16A8 8 0 0 0 8 0zm0 1.5a6.5 6.5 0 0 1 5.6 3.2H10.8c-0.5-1.3-1.4-2.4-2.8-3.2zM3 4.7A6.5 6.5 0 0 1 6.6 1.7C5.9 2.5 5.3 3.5 5 4.7zM1.5 8c0-0.6 0.1-1.2 0.3-1.8h2.9a11 11 0 0 0 0 3.6H1.8A6.5 6.5 0 0 1 1.5 8zm4.7 0c0-0.6 0-1.2 0.1-1.8h3.4a10 10 0 0 1 0 3.6H6.3C6.2 9.2 6.2 8.6 6.2 8zm5.1-1.8h2.9a6.5 6.5 0 0 1 0 3.6h-2.9a11 11 0 0 0 0-3.6zM3 11.3h2c0.3 1.2 0.9 2.2 1.6 3A6.5 6.5 0 0 1 3 11.3zm3.6 0h2.8c-0.3 1.1-0.8 2.1-1.4 2.9-0.6-0.8-1.1-1.8-1.4-2.9zm4.2 0h2.8a6.5 6.5 0 0 1-3.6 3c0.4-0.8 0.7-1.8 0.8-3z"/></svg>
          <span>www.brivomatex.example</span>
        </li>
      </ul>
    </div>
  </section>
</main>
</body>
</html>
```